Termite Mailer September 2021

We need a clean modern looking flyer advertising termites via the mail.

Size should be 9"x6"

Our tagline is "The Smarter Approach to Pest Control"

Something along the stylistic design of these:

https://pics.hollowmarsh.example/Qa83LkTzWp

https://pics.hollowmarsh.example/Rn47VbXcMd

https://pics.hollowmarsh.example/Hj29PsYeUf

https://www.flintquillprint.example/wp-content/uploads/designs/img/Pest-Prevention-Postcard-PST-1003.jpg

Should include some of this verbiage:

HAVE YOU SCHEDULED YOUR ANNUAL TERMITE INSPECTION? - MAKE IT IN RED

DON'T WAIT. PROTECT YOUR HOME TODAY!

ABSOLUTELY FREE INSPECTION. NO OBLIGATION.

TERMITES CAN CAUSE SEVERE DAMAGE TO YOUR HOME.

BRINDLEVALE LOGO

THE SMARTER APPROACH TO PEST CONTROL.

PROTECT YOUR MOST VALUABLE ASSET.

10% DISCOUNT ON ANY SERVICE GUARANTEED IF YOU CALL TODAY.

INCLUDE A PICTURE OF A TERMITE AS WELL SOMEWHERE AND WOOD DAMAGE.

Target Market(s)

Homeowners in Southern California USA

Industry/Entity Type

Pest Control/Extermination

Font styles to use
Other font styles liked:
• Chaparral Pro Italic, Brava Slab

Requirements
Must have
• Clean design, picture of house, picture of Termite, 10% off coupon and call to action on the back
Should not have
• Bad looking houses, colors that don't match our logo

```html
<!DOCTYPE html>
<html lang="en">
<head>
<meta charset="utf-8">
<title>Brindlevale Termite Mailer</title>
<link rel="stylesheet" href="https://fonts.googleapis.com/css2?family=Bitter:wght@800&family=Crimson+Pro:ital,wght@0,400;1,400&display=swap">
<style>
  :root {
    --page-bg: #e2e3e5;
    --card-bg: #ffffff;
    --alert-red: #e41e26;
    --brand-blue: #0872bb;
    --brand-green: #7bc143;
    --green-deep: #6aa83c;
    --ink: #231f20;
    --white: #ffffff;
    --wood-dark: #7a4733;
    --wood-mid: #a56a52;
    --wood-light: #c99a7c;
  }
  * { margin: 0; padding: 0; box-sizing: border-box; }
  html, body { width: 1200px; height: 1200px; overflow: hidden; }
  body { background: var(--page-bg); position: relative; font-family: "Crimson Pro", Georgia, serif; }

  .mailer {
    position: absolute; left: 109px; top: 272px;
    width: 983px; height: 655px;
    background: var(--card-bg); overflow: hidden;
  }

  .headline {
    position: absolute; left: 57px; top: 54px;
    font-family: "Bitter", Georgia, serif; font-weight: 800;
    font-size: 38px; line-height: 48px; color: var(--alert-red);
  }
  .subhead {
    position: absolute; left: 57px; top: 166px;
    font-style: italic; font-size: 27px; color: var(--brand-blue);
  }

  .benefits { position: absolute; left: 525px; top: 124px; list-style: none; }
  .benefits li {
    display: flex; align-items: center; gap: 7px;
    height: 26px; font-size: 19.5px; color: var(--ink);
  }
  .benefits svg { width: 19px; height: 19px; flex: none; }

  .photo-band {
    position: absolute; left: 0; top: 231px; width: 983px; height: 240px;
    background:
      linear-gradient(180deg, rgba(0,0,0,0) 0%, rgba(60,30,20,0.35) 48%, rgba(0,0,0,0) 60%),
      linear-gradient(100deg, var(--wood-mid) 0%, var(--wood-dark) 35%, var(--wood-mid) 65%, var(--wood-light) 100%);
  }

  .offer { position: absolute; left: 37px; top: 283px; width: 473px; }
  .offer-amount {
    height: 94px; background: var(--green-deep);
    font-family: "Bitter", Georgia, serif; font-weight: 800;
    font-size: 64px; line-height: 98px; color: var(--white);
    padding-left: 22px; letter-spacing: 0.5px;
  }
  .offer-terms {
    height: 44px; background: var(--brand-green);
    font-size: 23px; line-height: 42px; color: var(--white);
    padding-left: 21px;
  }

  .brand { position: absolute; left: 58px; top: 506px; display: flex; align-items: center; gap: 10px; }
  .brand-dot { width: 40px; height: 40px; border-radius: 50%; background: var(--brand-green); }
  .brand-name {
    font-family: "Bitter", Georgia, serif; font-weight: 800;
    font-size: 40px; color: var(--brand-blue); letter-spacing: 0.5px;
  }
  .brand-tagline {
    position: absolute; left: 57px; top: 585px;
    font-style: italic; font-size: 22px; color: var(--brand-blue);
  }

  .cta-panel { position: absolute; left: 0; top: 471px; width: 983px; height: 184px; }
  .cta-label {
    position: absolute; left: 498px; top: 529px;
    font-size: 23px; color: var(--white); letter-spacing: 0.3px;
  }
  .cta-phone {
    position: absolute; left: 522px; top: 558px;
    display: flex; align-items: center; gap: 8px;
    font-family: "Bitter", Georgia, serif; font-weight: 800;
    font-size: 48px; color: var(--white);
  }
  .cta-phone svg { width: 44px; height: 44px; }
</style>
</head>
<body>
  <main class="mailer">
    <h1 class="headline">Have You Scheduled Your Annual<br>Termite Inspection?</h1>
    <p class="subhead">Don’t Wait. Protect Your Home Today!</p>

    <ul class="benefits">
      <li><svg viewBox="0 0 20 20"><circle cx="10" cy="10" r="8.5" fill="none" stroke="#0872bb" stroke-width="1.6"/><path d="M6 10.3l2.8 2.7L14.2 7" fill="none" stroke="#7bc143" stroke-width="1.8"/></svg>Absolutely Free Inspection. No Obligation.</li>
      <li><svg viewBox="0 0 20 20"><circle cx="10" cy="10" r="8.5" fill="none" stroke="#0872bb" stroke-width="1.6"/><path d="M6 10.3l2.8 2.7L14.2 7" fill="none" stroke="#7bc143" stroke-width="1.8"/></svg>Termites can cause severe damage to your home.</li>
      <li><svg viewBox="0 0 20 20"><circle cx="10" cy="10" r="8.5" fill="none" stroke="#0872bb" stroke-width="1.6"/><path d="M6 10.3l2.8 2.7L14.2 7" fill="none" stroke="#7bc143" stroke-width="1.8"/></svg>Protect your most valuable asset.</li>
    </ul>

    <div class="photo-band" role="img" aria-label="Close-up photo of termites crawling through damaged, eaten wood"></div>

    <div class="offer">
      <div class="offer-amount">10% Discount</div>
      <div class="offer-terms">On any service guaranteed if you call today.</div>
    </div>

    <svg class="cta-panel" viewBox="0 0 983 184" preserveAspectRatio="none">
      <polygon points="424,0 438,0 487,184 473,184" fill="#7bc143"/>
      <polygon points="438,0 983,0 983,184 487,184" fill="#0872bb"/>
    </svg>

    <div class="brand">
      <span class="brand-dot"></span>
      <span class="brand-name">BRINDLEVALE</span>
    </div>
    <p class="brand-tagline">The Smarter Approach to Pest Control</p>

    <p class="cta-label">CLAIM YOUR LIMITED TIME DISCOUNT!</p>
    <p class="cta-phone">
      <svg viewBox="0 0 24 24"><path fill="#ffffff" d="M6.6 10.8c1.4 2.8 3.8 5.1 6.6 6.6l2.2-2.2c.3-.3.7-.4 1-.2 1.1.4 2.3.6 3.6.6.6 0 1 .4 1 1V20c0 .6-.4 1-1 1C10.6 21 3 13.4 3 4c0-.6.4-1 1-1h3.5c.6 0 1 .4 1 1 0 1.3.2 2.5.6 3.6.1.3 0 .7-.2 1l-2.3 2.2z"/></svg>
      (714) 555-0148
    </p>
  </main>
</body>
</html>
```